Need a banner for trees, and shrubs at our lanscape supply yard see attached logo

Need a nice banner to showcase our new addition of trees and shrubs for our customers.

```html
<!DOCTYPE html>
<html lang="en">
<head>
<meta charset="utf-8">
<title>Grove 18 Supply – Trees &amp; Shrubs Banner</title>
<link href="https://fonts.googleapis.com/css2?family=Alfa+Slab+One&family=Old+Standard+TT:wght@700&display=swap" rel="stylesheet">
<style>
  :root {
    --white: #ffffff;
    --brand-red: #6b1f22;
    --leaf-green: #0f9444;
    --leaf-light: #3fb26a;
    --panel-green: #10763c;
    --panel-accent: #14884a;
    --text-light: #ffffff;
  }
  html, body {
    margin: 0;
    padding: 0;
    overflow: hidden;
    background: var(--white);
  }
  .banner {
    position: relative;
    width: 1200px;
    height: 364px;
    background: var(--white);
    overflow: hidden;
    font-family: "Alfa Slab One", Georgia, serif;
  }
  .tree-emblem {
    position: absolute;
    left: 62px;
    top: 26px;
    width: 216px;
    height: 216px;
    border-radius: 50%;
    background: radial-gradient(circle at 45% 40%, var(--leaf-light), var(--leaf-green) 70%);
  }
  .brand-name {
    margin: 0;
    font-weight: 400;
  }
  .brand-name__main {
    position: absolute;
    left: 149px;
    top: 150px;
    font-size: 128px;
    line-height: 1;
    letter-spacing: -2px;
    white-space: nowrap;
    color: var(--brand-red);
  }
  .brand-name__sub {
    position: absolute;
    left: 112px;
    top: 284px;
    font-size: 57px;
    line-height: 1;
    letter-spacing: 18px;
    white-space: nowrap;
    color: var(--leaf-green);
  }
  .rule-stack {
    position: absolute;
    left: 488px;
    top: 292px;
    width: 319px;
  }
  .rule-stack span {
    display: block;
    height: 5px;
    background: var(--leaf-green);
    margin-bottom: 13px;
  }
  .contact-panel {
    position: absolute;
    left: 843px;
    top: 0;
    width: 357px;
    height: 364px;
    background: var(--panel-green);
    color: var(--text-light);
    font-family: "Old Standard TT", Georgia, serif;
    font-weight: 700;
  }
  .contact-panel__emblem {
    position: absolute;
    left: 52px;
    top: 34px;
    width: 270px;
    height: 270px;
    border-radius: 50%;
    background: var(--panel-accent);
    opacity: 0.8;
  }
  .contact-panel__label,
  .contact-panel__phone {
    position: absolute;
    left: 0;
    width: 370px;
    margin: 0;
    text-align: center;
    line-height: 1;
    white-space: nowrap;
  }
  .contact-panel__label {
    top: 207px;
    font-size: 27px;
    letter-spacing: 1px;
  }
  .contact-panel__phone {
    top: 232px;
    width: 366px;
    font-size: 42px;
    letter-spacing: 1px;
  }
  .social-list {
    position: absolute;
    top: 282px;
    left: 60px;
    display: flex;
    gap: 21px;
    margin: 0;
    padding: 0;
    list-style: none;
  }
  .social-list__item {
    width: 46px;
    height: 46px;
    border-radius: 50%;
    background: var(--leaf-green);
    box-shadow: 3px 4px 6px rgba(0, 0, 0, 0.25);
    display: flex;
    align-items: center;
    justify-content: center;
    font-size: 8px;
    color: var(--text-light);
  }
</style>
</head>
<body>
  <div class="banner">
    <div class="tree-emblem" role="img" aria-label="Leafy green tree emblem with red-brown trunk for the new trees and shrubs range"></div>
    <h1 class="brand-name">
      <span class="brand-name__main">GROVE 18</span>
      <span class="brand-name__sub">SUPPLY</span>
    </h1>
    <div class="rule-stack" aria-hidden="true">
      <span></span><span></span><span></span>
    </div>
    <aside class="contact-panel">
      <div class="contact-panel__emblem" role="img" aria-label="Faint tree canopy of leaves"></div>
      <p class="contact-panel__label">Help Line:</p>
      <p class="contact-panel__phone">+12-40917</p>
      <ul class="social-list">
        <li class="social-list__item">Fernly</li>
        <li class="social-list__item">Snapleaf</li>
        <li class="social-list__item">Linkroot</li>
        <li class="social-list__item">Chatbud</li>
      </ul>
    </aside>
  </div>
</body>
</html>
```